Postcard Design

I need a postcard style insert designed that will be mailed out with a customer's monthly statement. This postcard will describe a new service offered to the customer by our company. The front of the postcard will have a design layout of the word definition for "Monetize" and similar to design layout used in a dictionary (i.e., enunciation, Verb, definition, and sample of how word is used). The backside of card will have brief description of service offered and contact information for my office.

It Company

```html
<!DOCTYPE html>
<html lang="en">
<head>
<meta charset="utf-8">
<title>Monetize Postcard</title>
<link href="https://fonts.googleapis.com/css2?family=Arimo:wght@400;700&family=Gochi+Hand&display=swap" rel="stylesheet">
<style>
  :root {
    --stage: #333333;
    --paper: #ffffff;
    --orange: #e6830a;
    --navy: #1f2147;
    --red: #e8301c;
    --ink: #1f2147;
    --cream: #ffffff;
    --fine: #2a1a08;
  }
  * { margin: 0; padding: 0; box-sizing: border-box; }
  html, body { width: 1200px; height: 652px; overflow: hidden; background: var(--stage); }
  .canvas { position: relative; width: 1200px; height: 652px; font-family: "Arimo", Arial, sans-serif; }
  .postcard { position: absolute; left: 123px; top: 142px; width: 953px; height: 367px; display: flex; overflow: hidden; }
  .front { position: relative; width: 476px; height: 100%; background: var(--paper); overflow: hidden; }
  .back { position: relative; width: 477px; height: 100%; background: var(--orange); }
  .book-art { position: absolute; left: 0; top: 0; width: 476px; height: 367px; }
  .brand-mark { position: absolute; display: flex; align-items: center; gap: 6px; color: var(--navy); font-weight: 700; line-height: 1.05; text-transform: uppercase; }
  .brand-mark .dot { flex: none; background: var(--navy); border-radius: 50%; }
  .brand-front { left: 44px; top: 52px; font-size: 11px; }
  .brand-front .dot { width: 14px; height: 14px; }
  .brand-back { left: 40px; top: 240px; font-size: 17px; }
  .brand-back .dot { width: 22px; height: 22px; }
  .definition { position: absolute; left: 122px; top: 202px; transform: rotate(-13deg); transform-origin: left top; color: var(--ink); }
  .headword { font-family: "Gochi Hand", cursive; font-size: 58px; line-height: 1; letter-spacing: 1px; color: #201a2e; }
  .pronunciation { font-size: 13px; color: var(--red); margin: 6px 0 0 48px; }
  .part-of-speech { font-size: 13px; color: var(--red); margin: 8px 0 0 50px; }
  .senses { list-style: none; font-size: 12px; line-height: 1.3; margin: 2px 0 0 52px; }
  .senses .cont { padding-left: 14px; }
  .pitch { position: absolute; left: 34px; top: 38px; color: var(--cream); font-size: 11px; line-height: 16.4px; }
  .privacy { position: absolute; left: 16px; top: 333px; font-size: 8px; color: var(--fine); white-space: nowrap; }
</style>
</head>
<body>
<main class="canvas">
  <section class="postcard">
    <div class="front">
      <svg class="book-art" viewBox="0 0 476 367" role="img" aria-label="Open antique dictionary with aged tan pages, photographed at an angle">
        <defs>
          <linearGradient id="pageTone" x1="0" y1="0" x2="1" y2="1">
            <stop offset="0" stop-color="#e2b779"/>
            <stop offset="0.55" stop-color="#d6a265"/>
            <stop offset="1" stop-color="#b97f43"/>
          </linearGradient>
        </defs>
        <polygon points="56,152 476,36 476,367 124,367" fill="#d9dcdc"/>
        <polygon points="66,160 476,46 476,367 132,367" fill="#2a2a2a"/>
        <polygon points="76,164 476,52 476,367 140,367" fill="url(#pageTone)"/>
      </svg>
      <div class="brand-mark brand-front"><span class="dot"></span><span>Harbor Lane<br>Realty</span></div>
      <div class="definition">
        <p class="headword">mon·e·tize</p>
        <p class="pronunciation">/ˈmäne.tīz/</p>
        <p class="part-of-speech">verb</p>
        <ol class="senses">
          <li>1.Convert into or express in the form of currency.</li>
          <li>2.Convert real estate contract into currency that</li>
          <li class="cont">can be used to purchase goods and services</li>
        </ol>
      </div>
    </div>
    <div class="back">
      <p class="pitch">
        Interested in knowing what your<br>
        real estate contract is worth if you<br>
        were to sell it for a lump sum<br>
        cash payment?<br>
        Call Note Buyers Group today<br>
        at 555-014-2290<br>
        for a free no-obligation quote<br>
        on the cash value of your contract.
      </p>
      <div class="brand-mark brand-back"><span class="dot"></span><span>Harbor Lane<br>Realty</span></div>
      <p class="privacy">Your privacy is assured.&nbsp; Your escrow servicing providing this opportunity to you as a confidential courtesy</p>
    </div>
  </section>
</main>
</body>
</html>
```